New south Australia high-end red wine label & logo design

Marvick Estate exports premium south Australian wine to oversea market. We are looking for a professional graphic designer to design a full set of wine label and logo for our new red wine, the label & logo should look 'high-end' & Luxury and attractive. Black & gold color is preferred. I have attached example images to demonstrate the feel that we are looking for. These are just a possible starting point. The expectation is that the label would be professional/polished. I am open to any and all designs that would alter my perception of what will be best!

Target customer -

we need the label to be print-ready.

There will be 3 parts to this design.

Top Cover design with gold text wrapped, the front label and the back label

-Brand name Marvik Estate
-text wine of Australia
-text Cabernet
-Year 2015
-text Sourced from premium Australian wine growing region Merrigal valley

Look and Feel:
• Elegant
• Serious
• Modern/Traditional
• Professional
• Gender Neutral
• Upmarket

--------------Back Label text---------------
Rich and opulent with intense fruit aromas of black berry, liquorice and cassis with hints of dark chocolate and pungent spices. Sumptuous and textured palate with beautifully detailed ripe black fruits flowing seamlessly across the palate. French oak provides a complex harmony and finish of great length, balance and purity.

Produced by Rolk Haven Group International Pty Ltd
27 Fellmore Road,Quandip, South Australia, 5172
14.5 ALC/VOL
Wine of Australia
Approx 8.3 Standard Drinks
Contains Sulphites
750 ML
Please leave the space for Bar Code

Requirements
Must have
• wine name, wine logo, wine type etc (should include all 'must-have the required fields wine lable)
Nice to have
• Desginer's own idea
Should not have
• should not be too playful

```html
<!DOCTYPE html>
<html lang="en">
<head>
<meta charset="utf-8">
<title>Marvik Estate – Cabernet 2015 Labels</title>
<link rel="stylesheet" href="https://fonts.googleapis.com/css2?family=Cinzel:wght@400;600;700&family=Josefin+Sans:wght@700&family=Poiret+One&family=Tinos&display=swap">
<style>
  :root{
    --ink:#000000;
    --gold:#c9a24c;
    --gold-light:#e2c27f;
    --gold-deep:#9c7a2e;
    --paper:#ffffff;
  }
  *{margin:0;padding:0;box-sizing:border-box}
  html,body{width:1063px;height:1200px;overflow:hidden;background:var(--paper)}
  .sheet{position:relative;width:1063px;height:1200px}
  .label{position:absolute;top:0;height:1200px;width:481px;background:var(--ink);border:8px solid var(--gold-light)}
  .label--front{left:0}
  .label--back{left:582px}
  .rule{position:absolute;left:0;right:0;height:3px;background:var(--gold-light)}
  .flourish{position:absolute;width:160px;height:290px;opacity:.35;
    background:radial-gradient(ellipse at center,var(--gold-deep) 0%,rgba(156,122,46,.25) 45%,rgba(0,0,0,0) 75%)}
  .gold{color:var(--gold);position:absolute;white-space:nowrap}
  .center-x{left:50%;transform:translateX(-50%)}
  .rotated{transform:translate(-50%,-50%) rotate(-90deg)}

  /* front */
  .brand-vertical{left:241px;top:574px;font-family:"Cinzel",serif;font-weight:700;font-size:70px;letter-spacing:2px;line-height:1}
  .sourced{left:321px;top:574px;font-family:"Tinos",serif;font-size:18px;line-height:1}
  .region{left:363px;top:574px;font-family:"Tinos",serif;font-size:17px;text-decoration:underline;text-transform:uppercase;line-height:1}
  .mark-front{left:106px;top:591px;display:flex;align-items:center;gap:10px;font-family:"Cinzel",serif;font-size:16px;font-weight:600}
  .mark-square{width:20px;height:20px;border:2px solid var(--gold)}
  .varietal-front{top:1003px;font-family:"Cinzel",serif;font-weight:700;font-size:22px;letter-spacing:3px}
  .vintage{top:1048px;font-family:"Cinzel",serif;font-weight:700;font-size:32px;letter-spacing:3px}
  .origin-front{top:1127px;font-family:"Cinzel",serif;font-weight:600;font-size:16px;letter-spacing:1px}

  /* back */
  .mark-back{top:110px;width:110px;height:110px;border:2px solid var(--gold)}
  .brand-back{top:255px;font-family:"Cinzel",serif;font-weight:700;font-size:46px;letter-spacing:1px}
  .wine-name{top:355px;font-family:"Cinzel",serif;font-weight:700;font-size:27px;letter-spacing:2px}
  .info{font-family:"Poiret One",sans-serif;font-size:18px;font-weight:400}
  .contains{top:414px}
  .produced{top:456px}
  .producer{top:498px}
  .address{top:541px;text-align:center;line-height:21px}
  .tasting{position:absolute;left:22px;width:422px;top:612px;color:var(--gold);font-family:"Poiret One",sans-serif;font-size:17.5px;line-height:23.3px;text-align:justify;text-align-last:justify}
  .origin-back{top:792px;font-family:"Josefin Sans",sans-serif;font-weight:700;font-size:22px;letter-spacing:.5px}
  .drinks{top:837px;font-family:"Tinos",serif;font-size:21px;letter-spacing:2.5px}
  .barcode-space{position:absolute;left:87px;top:899px;width:292px;height:131px;background:var(--paper)}
  .volume{top:1052px;font-family:"Tinos",serif;font-size:34px}
  .varietal-back{top:1127px;font-family:"Cinzel",serif;font-weight:700;font-size:30px;letter-spacing:4px}
</style>
</head>
<body>
<main class="sheet">

  <section class="label label--front" aria-label="Front label">
    <div class="rule" style="top:47px"></div>
    <div class="rule" style="top:1103px"></div>
    <div class="rule" style="top:1171px"></div>

    <div class="flourish" style="left:5px;top:55px" role="img" aria-label="Gold scroll flourish ornament"></div>
    <div class="flourish" style="right:5px;top:55px" role="img" aria-label="Gold scroll flourish ornament"></div>
    <div class="flourish" style="left:5px;top:805px" role="img" aria-label="Gold scroll flourish ornament"></div>
    <div class="flourish" style="right:5px;top:805px" role="img" aria-label="Gold scroll flourish ornament"></div>

    <div class="gold mark-front rotated"><span class="mark-square"></span><span>Marvik Estate</span></div>
    <h1 class="gold brand-vertical rotated">Marvik Estate</h1>
    <p class="gold sourced rotated">Sourced from Premium Australian Wine growing region.</p>
    <p class="gold region rotated">Merrigal Valley</p>

    <p class="gold varietal-front center-x">CABERNET</p>
    <p class="gold vintage center-x">2015</p>
    <p class="gold origin-front center-x">WINE OF AUSTRALIA</p>
  </section>

  <section class="label label--back" aria-label="Back label">
    <div class="rule" style="top:47px"></div>
    <div class="rule" style="top:1103px"></div>
    <div class="rule" style="top:1171px"></div>

    <div class="gold mark-back center-x"></div>
    <h2 class="gold brand-back center-x">Marvik Estate</h2>
    <p class="gold wine-name center-x">BLACK&nbsp; FRUITS</p>
    <p class="gold info contains center-x">Contains: Sulphites</p>
    <p class="gold info produced center-x">Produced by</p>
    <p class="gold info producer center-x">Rolk Haven Group International Pty Ltd</p>
    <p class="gold info address center-x">27 Fellmore Road,Quandip<br>South Australia, 5172</p>
    <p class="tasting">Rich and opulent with intense fruit aromas of Black Berry, Liquorice and Cassis with hints of dark chocolate and pungent spices. Sumptuous and textured palate with beautifully detailed ripe black fruits flowing seamlessly across the palate. French oak provides a complex</p>
    <p class="gold origin-back center-x">WINE OF AUSTRALIA</p>
    <p class="gold drinks center-x">Approx 8.3 Standard Drinks</p>
    <div class="barcode-space" aria-label="Reserved space for barcode"></div>
    <p class="gold volume center-x">750 ml</p>
    <p class="gold varietal-back center-x">CABERNET</p>
  </section>

</main>
</body>
</html>
```